Real Estate 24"x24" Sign, Business Card, Letter Head and Envelope

This is a 4 project contest. If we choose a design or designs we like from what you sent we are willing to pay an amount at our discretion for that design even if we don't like all your designs for the 4 projects. Please be creative. Attached are our logo files. Please message us with any questions. Thanks and Good Luck!
Project 1: QLTV Realty 24" x 24" yard sign
We want to use the same blue background in our logo for the sign where the logo in white font will be on. CMYK 100,80,0,0. Attached is a sample a local designer made for you to get an idea what we are looking for. In the sample, the website is way too big and the entire sign is very plain and not attractive looking plus blue color is wrong one. We want the logo on top as large as possible but keeping it proportionate and attractive looking buy not too big that it looks odd. The following information can go in white color background or same blue color background color. Our company colors are blue (as per logo), green (as per logo), and white. "Residential & Commercial" goes under the logo. Under that put our phone number "312-948-6051" as large as possible but still looks good and under that our website in much smaller but readable font "www.qltvrealty.com".
Project 2: Envelope
We have two version of the logo. Use one or both. Whatever looks best in your design. The envelope will be white. We only want on top left corner logo and underneath our mailing address: 5197 Larchmere Ave. Skokie, IL 60093-1725. Maybe some creative decorative design at bottom of envelope will look nice
Project 3: Letter Head
We have two version of the logo. Use one or both. Whatever looks best in your design. We want the following information on the top of the letterhead. Logo, address: 5197 Larchmere Ave., Skokie, IL 60093-1725, phone: 312-948-6051, fax: 312-682-9307 website www.qltvrealty.com, email: info@qltvrealty.com
Project 4: Business card
Use either logo. We need cards for two individuals. Information for Person 1: Dev Kulkarni, Managing Broker, Phone: 312-948-6051, Email: dev.kulkarni@qltvrealty.com. Person 2: Ajay Kulkarni Broker Phone: 312-519-8263 Email: ajay.kulkarni@qltvrealty.com. Add Address, Fax and website same as above letter head.

```html
<!DOCTYPE html>
<html lang="en">
<head>
<meta charset="utf-8">
<title>QLTV Realty – Yard Sign</title>
<link rel="stylesheet" href="https://fonts.googleapis.com/css2?family=Montserrat:wght@300;800;900&display=swap">
<style>
  :root {
    --brand-blue: #0350a3;
    --paper: #ffffff;
  }
  * { margin: 0; padding: 0; box-sizing: border-box; }
  html, body {
    width: 1200px;
    height: 1189px;
    overflow: hidden;
    background: var(--paper);
  }
  .sign {
    position: relative;
    width: 1200px;
    height: 1189px;
    background: var(--paper);
    font-family: "Montserrat", sans-serif;
  }
  .sign__panel {
    position: absolute;
    left: 0; top: 0;
    width: 1200px;
    height: 866px;
    background: var(--brand-blue);
  }
  .brand-name {
    position: absolute;
    left: 0; right: 0;
    top: 290px;
    display: flex;
    align-items: center;
    justify-content: center;
    gap: 34px;
    color: var(--paper);
    font-weight: 800;
    font-size: 124px;
    line-height: 1;
    letter-spacing: 1px;
    white-space: nowrap;
  }
  .brand-name__mark {
    width: 70px;
    height: 70px;
    background: var(--paper);
  }
  .tagline {
    position: absolute;
    left: 0; right: 0;
    top: 700px;
    text-align: center;
    color: var(--paper);
    font-weight: 800;
    font-size: 87px;
    line-height: 1;
    white-space: nowrap;
  }
  .contact {
    position: absolute;
    left: 304px;
    top: 950px;
    height: 197px;
    border-left: 20px solid var(--brand-blue);
    padding-left: 33px;
    color: var(--brand-blue);
  }
  .contact__phone {
    margin-top: 12px;
    font-weight: 900;
    font-size: 78px;
    line-height: 1;
    letter-spacing: 2px;
    white-space: nowrap;
  }
  .contact__web {
    margin-top: 18px;
    font-weight: 300;
    font-size: 60px;
    line-height: 1;
    white-space: nowrap;
  }
</style>
</head>
<body>
  <main class="sign">
    <section class="sign__panel">
      <div class="brand-name">
        <span class="brand-name__mark" aria-hidden="true"></span>
        <span>QLTV Realty</span>
      </div>
      <p class="tagline">Residential &amp; Commercial</p>
    </section>
    <section class="contact">
      <p class="contact__phone">312-948-6051</p>
      <p class="contact__web">qltvrealty.com</p>
    </section>
  </main>
</body>
</html>
```